New Business Card Design Project

Removed as project is complete.

Target Market(s)

Industry/Entity Type

Business

Requirements
Must have
• Removed as project is complete.
Nice to have
Should not have

```html
<!DOCTYPE html>
<html lang="en">
<head>
<meta charset="utf-8">
<title>Emberline Compliance – Business Card</title>
<link rel="stylesheet" href="https://fonts.googleapis.com/css2?family=Alfa+Slab+One&family=Crimson+Text:wght@400;600&family=Arimo:wght@400;700&display=swap">
<style>
  :root {
    --backdrop: #e9e6e2;
    --card-dark: #2a2a2a;
    --card-dark-edge: #1e1e1e;
    --card-light: #f7f7f7;
    --card-light-shade: #e3e3e3;
    --bar-light: #e9e4e2;
    --bar-dark: #505050;
    --text-light: #f2f2f2;
    --text-soft: #d8d8d8;
    --brand-orange: #d9821c;
    --tagline: #3a3a3a;
  }
  * { margin: 0; padding: 0; box-sizing: border-box; }
  html, body {
    width: 1200px; height: 1067px; overflow: hidden;
    background: var(--backdrop);
  }
  .stage {
    position: relative; width: 1200px; height: 1067px;
  }
  .card {
    position: absolute; top: 166px; width: 420px; height: 735px;
    box-shadow: 0 10px 30px rgba(0,0,0,.25);
    overflow: hidden;
  }
  /* Back: contact side */
  .card--back {
    left: 150px;
    background: radial-gradient(circle at 40% 85%, #3a3a3a 0%, var(--card-dark) 45%, var(--card-dark-edge) 100%);
  }
  .accent-bars { position: absolute; }
  .accent-bars--left { left: 0; top: 100px; }
  .accent-bars--right { right: 0; top: 470px; }
  .contact-list {
    position: absolute; left: 68px; top: 44px;
    list-style: none;
    font-family: "Crimson Text", serif; font-size: 16px;
    color: var(--text-light); line-height: 34px;
  }
  .person {
    position: absolute; left: 0; right: 0; top: 400px;
    text-align: center; padding-left: 40px;
  }
  .person__name {
    font-family: "Alfa Slab One", serif; font-size: 34px;
    font-weight: 400; letter-spacing: 1px;
    color: var(--text-light);
  }
  .person__role, .person__degree {
    font-family: "Crimson Text", serif; font-size: 24px;
    color: var(--text-soft); line-height: 36px;
  }
  .person__role { margin-top: 10px; }

  /* Front: brand side */
  .card--front {
    left: 630px;
    background: radial-gradient(circle at 55% 40%, #ffffff 0%, var(--card-light) 40%, var(--card-light-shade) 100%);
  }
  .brand {
    position: absolute; left: 30px; right: 30px; top: 300px;
    display: flex; align-items: center; gap: 14px;
  }
  .brand__dot {
    width: 44px; height: 44px; border-radius: 50%;
    background: var(--brand-orange); flex: none;
  }
  .brand__text { font-family: "Arimo", sans-serif; }
  .brand__name {
    font-size: 31px; font-weight: 700; color: var(--brand-orange);
    letter-spacing: -.5px; line-height: 1.1;
  }
  .brand__tagline {
    font-size: 16px; color: var(--tagline); margin-top: 4px;
  }
</style>
</head>
<body>
<main class="stage">
  <section class="card card--back" aria-label="Card back with contact details">
    <svg class="accent-bars accent-bars--left" width="62" height="200" aria-hidden="true">
      <rect x="0" y="0" width="18" height="200" fill="var(--bar-light)"/>
      <rect x="34" y="0" width="28" height="200" fill="var(--bar-light)"/>
    </svg>
    <ul class="contact-list">
      <li>Person's Mobile: +61 (0)400 555 018</li>
      <li>email: contact@emberlinecompliance.com</li>
      <li>www.emberlinecompliance.com</li>
    </ul>
    <div class="person">
      <h1 class="person__name">Daniel Hartley</h1>
      <p class="person__role">Director</p>
      <p class="person__degree">BBus</p>
    </div>
  </section>

  <section class="card card--front" aria-label="Card front with company name">
    <div class="brand">
      <span class="brand__dot" aria-hidden="true"></span>
      <div class="brand__text">
        <p class="brand__name">Emberline Compliance</p>
        <p class="brand__tagline">Clearing the way to compliance...</p>
      </div>
    </div>
    <svg class="accent-bars accent-bars--right" width="56" height="120" aria-hidden="true">
      <rect x="0" y="0" width="18" height="120" fill="var(--bar-dark)"/>
      <rect x="32" y="0" width="24" height="120" fill="var(--bar-dark)"/>
    </svg>
  </section>
</main>
</body>
</html>
```